Academic and Business book cover

I need a book cover for my academic and business book.
The focus is in international / global negotiation and influence (how to negotiate across cultures).
The book will be published on Brevora, both in Lumaro and printed edition. therefore I need something that works under Brevora guidelines.The final design should be elegant and still be able to stand out against the competition.
I would like to have orange+grey for the text colors on the cover, even if different options are welcome.
Title and my name are in the attached word doc.

Target Market(s)

graduates, Phds, from international business schools. Managers

Industry/Entity Type

Business

Font styles to use
Serif
Sans Serif

Colors

Requirements
Must have
• The title and my name should have elegant fonts.
Nice to have
• pictures of the world that don't have the "usual" Europe in the centre.

```html
<!DOCTYPE html>
<html lang="en">
<head>
<meta charset="utf-8">
<title>The 3Rs Blueprint – Cover Options</title>
<link rel="stylesheet" href="https://fonts.googleapis.com/css2?family=Inter:wght@400;500;600;700&display=swap">
<style>
  :root {
    --canvas: #ffffff;
    --option-number: #a3a3a3;
    --title-orange: #f5a12a;
    --subtitle: #f2f2f2;
    --cover-w: 269px;
    --cover-h: 398px;
  }
  * { margin: 0; padding: 0; box-sizing: border-box; }
  html, body {
    width: 1200px;
    height: 960px;
    overflow: hidden;
    background: var(--canvas);
    font-family: "Inter", "Helvetica Neue", Arial, sans-serif;
  }
  .sheet { position: relative; width: 1200px; height: 960px; }

  .option-number {
    position: absolute;
    transform: translate(-50%, -50%);
    font-size: 42px;
    font-weight: 600;
    color: var(--option-number);
    line-height: 1;
  }
  .cover {
    position: absolute;
    width: var(--cover-w);
    height: var(--cover-h);
    display: block;
  }

  /* colour schemes */
  .cover--one   { --bg:#1e1f27; --tab:#2f4561; --column:#5f8a3a; --band:#2c5b8c; --quad-a:#a87038; --quad-b:#a14a6b; --globe-a:#1fb5a8; --globe-b:#3b2f9c; --author-weight:600; }
  .cover--two   { --bg:#29292b; --tab:#45384f; --column:#5a9055; --band:#6b437d; --quad-a:#b07a3a; --quad-b:#a24d6c; --globe-a:#d7a3d8; --globe-b:#6e2a63; --author-weight:600; }
  .cover--three { --bg:#17171f; --tab:#2d4360; --column:#2d6298; --band:#4b937c; --quad-a:#c3782e; --quad-b:#a24b70; --globe-a:#e9c43a; --globe-b:#d8806a; --author-weight:600; }
  .cover--four  { --bg:#2b2b2d; --tab:#555457; --column:#6c3a5c; --band:#6b8c3a; --quad-a:#b8732e; --quad-b:#5f6f9e; --globe-a:#ece21e; --globe-b:#6fb6a0; --author-weight:400; }

  .cover .bg      { fill: var(--bg); }
  .cover .tab     { fill: var(--tab); }
  .cover .column  { fill: var(--column); opacity: .9; }
  .cover .band    { fill: var(--band); opacity: .9; }
  .cover .quad-a  { fill: var(--quad-a); opacity: .85; }
  .cover .quad-b  { fill: var(--quad-b); opacity: .85; }
  .cover .overlap { fill: var(--column); opacity: .45; }
  .cover .globe   { opacity: .72; }

  .cover .title {
    fill: var(--title-orange);
    font-size: 20px;
    font-weight: 600;
    text-anchor: middle;
  }
  .cover .subtitle {
    fill: var(--subtitle);
    font-size: 13.6px;
    font-weight: 500;
    letter-spacing: .5px;
    text-anchor: middle;
  }
  .cover .author {
    fill: var(--title-orange);
    font-size: 14.5px;
    font-weight: var(--author-weight);
    letter-spacing: .2px;
    text-anchor: middle;
  }
</style>
</head>
<body>
<main class="sheet">

  <span class="option-number" style="left:153px; top:73px;">1</span>
  <span class="option-number" style="left:697px; top:73px;">2</span>
  <span class="option-number" style="left:148px; top:540px;">3</span>
  <span class="option-number" style="left:698px; top:540px;">4</span>

  <!-- option 1 -->
  <svg class="cover cover--one" style="left:184px; top:53px;" viewBox="0 0 287 425" aria-label="Cover option 1">
    <defs>
      <radialGradient id="globe-one" cx="40%" cy="38%" r="70%">
        <stop offset="0" stop-color="var(--globe-a)"/>
        <stop offset="1" stop-color="var(--globe-b)"/>
      </radialGradient>
    </defs>
    <rect class="bg" width="287" height="425"/>
    <rect class="tab" x="0" y="43" width="26" height="26"/>
    <rect class="tab" x="261" y="43" width="26" height="26"/>
    <text class="title" x="143.5" y="63">The 3Rs Blueprint</text>
    <text class="subtitle" x="143.5" y="93">Strategic Persuasion and Dealmaking</text>
    <text class="subtitle" x="145" y="115">Methods for Cross-Cultural Success</text>
    <rect class="quad-a" x="53" y="168" width="90" height="90"/>
    <rect class="quad-b" x="143" y="168" width="91" height="90"/>
    <rect class="quad-b" x="53" y="258" width="90" height="90"/>
    <rect class="quad-a" x="143" y="258" width="91" height="90"/>
    <rect class="column" x="98" y="133" width="90" height="250"/>
    <rect class="band" x="0" y="213" width="287" height="90"/>
    <rect class="overlap" x="98" y="213" width="90" height="90"/>
    <g role="img" aria-label="Globe view of the Americas">
      <circle class="globe" cx="144" cy="258" r="90" fill="url(#globe-one)"/>
    </g>
    <text class="author" x="143.5" y="405">Harjinder K. Malik</text>
  </svg>

  <!-- option 2 -->
  <svg class="cover cover--two" style="left:734px; top:53px;" viewBox="0 0 287 425" aria-label="Cover option 2">
    <defs>
      <radialGradient id="globe-two" cx="40%" cy="38%" r="70%">
        <stop offset="0" stop-color="var(--globe-a)"/>
        <stop offset="1" stop-color="var(--globe-b)"/>
      </radialGradient>
    </defs>
    <rect class="bg" width="287" height="425"/>
    <rect class="tab" x="0" y="43" width="26" height="26"/>
    <rect class="tab" x="261" y="43" width="26" height="26"/>
    <text class="title" x="143.5" y="63">The 3Rs Blueprint</text>
    <text class="subtitle" x="143.5" y="93">Strategic Persuasion and Dealmaking</text>
    <text class="subtitle" x="145" y="115">Methods for Cross-Cultural Success</text>
    <rect class="quad-a" x="53" y="168" width="90" height="90"/>
    <rect class="quad-b" x="143" y="168" width="91" height="90"/>
    <rect class="quad-b" x="53" y="258" width="90" height="90"/>
    <rect class="quad-a" x="143" y="258" width="91" height="90"/>
    <rect class="column" x="98" y="133" width="90" height="250"/>
    <rect class="band" x="0" y="213" width="287" height="90"/>
    <rect class="overlap" x="98" y="213" width="90" height="90"/>
    <g role="img" aria-label="Globe view of the Americas">
      <circle class="globe" cx="144" cy="258" r="90" fill="url(#globe-two)"/>
    </g>
    <text class="author" x="143.5" y="405">Harjinder K. Malik</text>
  </svg>

  <!-- option 3 -->
  <svg class="cover cover--three" style="left:184px; top:520px;" viewBox="0 0 287 425" aria-label="Cover option 3">
    <defs>
      <radialGradient id="globe-three" cx="40%" cy="38%" r="70%">
        <stop offset="0" stop-color="var(--globe-a)"/>
        <stop offset="1" stop-color="var(--globe-b)"/>
      </radialGradient>
    </defs>
    <rect class="bg" width="287" height="425"/>
    <rect class="tab" x="0" y="43" width="26" height="26"/>
    <rect class="tab" x="261" y="43" width="26" height="26"/>
    <text class="title" x="143.5" y="63">The 3Rs Blueprint</text>
    <text class="subtitle" x="143.5" y="93">Strategic Persuasion and Dealmaking</text>
    <text class="subtitle" x="145" y="115">Methods for Cross-Cultural Success</text>
    <rect class="quad-a" x="53" y="168" width="90" height="90"/>
    <rect class="quad-b" x="143" y="168" width="91" height="90"/>
    <rect class="quad-b" x="53" y="258" width="90" height="90"/>
    <rect class="quad-a" x="143" y="258" width="91" height="90"/>
    <rect class="column" x="98" y="133" width="90" height="250"/>
    <rect class="band" x="0" y="213" width="287" height="90"/>
    <rect class="overlap" x="98" y="213" width="90" height="90"/>
    <g role="img" aria-label="Globe view of the Americas">
      <circle class="globe" cx="144" cy="258" r="90" fill="url(#globe-three)"/>
    </g>
    <text class="author" x="143.5" y="405">Harjinder K. Malik</text>
  </svg>

  <!-- option 4 -->
  <svg class="cover cover--four" style="left:734px; top:520px;" viewBox="0 0 287 425" aria-label="Cover option 4">
    <defs>
      <radialGradient id="globe-four" cx="40%" cy="38%" r="70%">
        <stop offset="0" stop-color="var(--globe-a)"/>
        <stop offset="1" stop-color="var(--globe-b)"/>
      </radialGradient>
    </defs>
    <rect class="bg" width="287" height="425"/>
    <rect class="tab" x="0" y="43" width="26" height="26"/>
    <rect class="tab" x="261" y="43" width="26" height="26"/>
    <text class="title" x="143.5" y="63">The 3Rs Blueprint</text>
    <text class="subtitle" x="143.5" y="93">Strategic Persuasion and Dealmaking</text>
    <text class="subtitle" x="145" y="115">Methods for Cross-Cultural Success</text>
    <rect class="quad-a" x="53" y="168" width="90" height="90"/>
    <rect class="quad-b" x="143" y="168" width="91" height="90"/>
    <rect class="quad-b" x="53" y="258" width="90" height="90"/>
    <rect class="quad-a" x="143" y="258" width="91" height="90"/>
    <rect class="column" x="98" y="133" width="90" height="250"/>
    <rect class="band" x="0" y="213" width="287" height="90"/>
    <rect class="overlap" x="98" y="213" width="90" height="90"/>
    <g role="img" aria-label="Globe view of the Americas">
      <circle class="globe" cx="144" cy="258" r="90" fill="url(#globe-four)"/>
    </g>
    <text class="author" x="143.5" y="405">Harjinder K. Malik</text>
  </svg>

</main>
</body>
</html>
```